Business Card Design for Translation Company - Rush

Rush job for a business card designing for a company doing international translations, several Asian and western languages. Already have a logo design (see attached) to use as the basis of the business card design. For the card, we also need the full company name, address, email, and phone number. In addition, my name as I will be the one handing out the cards.

For the logo design, we think the white background would be best. But we will consider using the dark background if you have a great idea for it.

The attached jpeg design has just been approved, but the designer has not yet finalized the file. When we select our final applicant, we will send the finalized file. (Nothing changes except the quality of the data.)

The phone number may change and if so, we will send the new one when we select our applicant.

We must complete the entire process and have a design ready to go to print no later than 01:00 am August 3, New York (East Coast) time.

We look forward to your participation in the project,
Jon

Target Market(s)

Translation clients worldwide.

Industry/Entity Type

Business

Contact Information for Business Card

Company details:

Korvane Translations International, Ltd.

#276-3820 Welbury Crescent, Victoria, BC, Canada V9T4K2

jhadley@korvanetranslations-example.com

+1-888-647-2315

Font styles to use
Sans Serif

Requirements
Must have
• Company name, address, email and phone number.
• Also my name:
• Jonathan R. Hadley
• Director
Nice to have
• Not a demand, but please consider creatively using the horizontal bar.
Should not have
• Cluttered of jumbled appearance.

```html
<!DOCTYPE html>
<html lang="en">
<head>
<meta charset="utf-8">
<title>Korvane Translations – Business Card</title>
<link rel="stylesheet" href="https://fonts.googleapis.com/css2?family=Lato:wght@400;700;900&display=swap">
<style>
  :root {
    --orange: #ec7722;
    --orange-soft: #f9e6d7;
    --ink: #3d3d3d;
    --grey-soft: #ececee;
    --white: #ffffff;
    --backdrop: #e9e6e1;
  }
  * { box-sizing: border-box; margin: 0; padding: 0; }
  html, body {
    width: 1200px; height: 1024px; overflow: hidden;
    background: var(--backdrop);
    font-family: "Lato", Arial, sans-serif;
  }
  .sheet { position: relative; width: 1200px; height: 1024px; }
  .card {
    position: absolute; left: 250px; width: 700px; height: 400px;
    border-radius: 4px; overflow: hidden;
    box-shadow: 0 10px 30px rgba(0,0,0,.15);
  }
  .card--front { top: 80px; background: var(--white); }
  .card--back  { top: 544px; background: var(--orange); }

  .decor-area {
    position: absolute; left: 0; bottom: 0; width: 290px; height: 190px;
    background: linear-gradient(90deg, var(--grey-soft), var(--orange-soft));
  }

  .brand { position: absolute; display: flex; align-items: center; gap: 14px; }
  .brand__dot { width: 34px; height: 34px; border-radius: 50%; }
  .brand__name {
    font-weight: 700; font-size: 22px; letter-spacing: 2px;
    text-transform: uppercase; line-height: 1;
  }
  .brand__rule { position: absolute; height: 2px; }

  .card--front .brand { left: 44px; top: 44px; }
  .card--front .brand__dot { background: var(--orange); }
  .card--front .brand__name { color: var(--ink); }
  .card--front .brand__rule { left: 92px; top: 86px; width: 250px; background: var(--orange); }

  .contact {
    position: absolute; right: 44px; top: 150px; text-align: right;
    color: var(--ink); font-size: 15px; line-height: 1.45;
  }
  .contact__name { font-weight: 900; font-size: 19px; letter-spacing: 1px; text-transform: uppercase; }
  .contact__title { color: var(--orange); font-size: 15px; }
  .contact__rule { display: block; margin: 4px 0 12px auto; width: 200px; height: 2px; background: var(--orange); }
  .contact__address { margin-bottom: 16px; }
  .contact__label { color: var(--orange); }

  .card--back .brand { left: 96px; top: 150px; }
  .card--back .brand__dot { background: var(--white); }
  .card--back .brand__name { color: var(--white); font-size: 26px; }
  .card--back .brand__rule { left: 144px; top: 196px; width: 300px; background: var(--white); }
  .website {
    position: absolute; left: 144px; top: 214px;
    color: var(--white); font-size: 17px; font-style: italic; letter-spacing: .5px;
  }
</style>
</head>
<body>
<main class="sheet">
  <section class="card card--front" aria-label="Business card front">
    <div class="decor-area" role="img" aria-label="Faint enlarged brand decoration area"></div>
    <div class="brand">
      <span class="brand__dot"></span>
      <span class="brand__name">Korvane Translations</span>
    </div>
    <span class="brand__rule"></span>

    <div class="contact">
      <p class="contact__name">Jonathan R. Hadley</p>
      <p class="contact__title">Director</p>
      <span class="contact__rule"></span>
      <p class="contact__address">
        Korvane Translations International, Ltd.<br>
        #276-3820 Welbury Crescent, Victoria, BC<br>
        Canada V9T4K2
      </p>
      <p><span class="contact__label">Phone:</span> +1-888-647-2315</p>
      <p><span class="contact__label">E-mail:</span> jhadley@korvanetranslations-example.com</p>
    </div>
  </section>

  <section class="card card--back" aria-label="Business card back">
    <div class="brand">
      <span class="brand__dot"></span>
      <span class="brand__name">Korvane Translations</span>
    </div>
    <span class="brand__rule"></span>
    <p class="website">www.korvanetranslations-example.com</p>
  </section>
</main>
</body>
</html>
```